Business Card Design Project

Lorantte is a women fashion house focusing on youthful glamour.

We bring together unique designs, premium quality materials and top craftsmanship to deliver sophisticated yet playful glamour, fun and excitement to the confident woman.

We can sum up the brand identity in 3 words:
Glamour – Sophistication – Unique

Industry/Entity Type

Fashion

Requirements
Must have
• Nim Tressoli
nim.tressoli@lorantte-example.com
Mobile: 081 536 2947
Instragram: lorantte_label
Facebook: lorantte_label

Creative Director
Lorantte Co., LTD
TEL: 02 417 39 86
47 Mango Row, 2nd Floor , D Building , Thonburi Court , Soi Ratchada 29.
Upper Bangrak , Sathorn , Bangkok 10500 Thailand
www.lorantte-example.com

```html
<!DOCTYPE html>
<html lang="en">
<head>
<meta charset="utf-8">
<title>Lorantte Business Card</title>
<link href="https://fonts.googleapis.com/css2?family=Oxygen:wght@300;400&display=swap" rel="stylesheet">
<style>
  :root{
    --stage:#1b1b1c;
    --card-back:#4a4a4d;
    --magenta:#a8478f;
    --magenta-deep:#8e2f78;
    --magenta-light:#bd63a6;
    --text-light:#e9e9ea;
    --text-soft:#c9c9cc;
    --accent-pink:#c0508f;
    --white:#ffffff;
  }
  *{margin:0;padding:0;box-sizing:border-box}
  html,body{width:1200px;height:1134px;overflow:hidden;background:var(--stage)}
  body{font-family:"Oxygen",Arial,sans-serif;position:relative}
  .card{
    position:absolute;width:560px;height:320px;
    border-radius:0 80px 0 80px;overflow:hidden;
  }
  .card-back{left:25px;top:407px;background:var(--card-back)}
  .card-front{left:615px;top:407px;background:linear-gradient(135deg,var(--magenta-light),var(--magenta) 55%,var(--magenta-deep))}
  .card-curves{position:absolute;inset:0;width:100%;height:100%}
  .holder{position:absolute;left:48px;top:58px;color:var(--text-light)}
  .holder-name{font-size:24px;font-weight:300;letter-spacing:.5px}
  .holder-title,.holder-company{font-size:14px;font-weight:300;color:var(--text-soft);margin-top:4px}
  .divider{position:absolute;left:282px;top:52px;width:1px;height:140px;background:var(--accent-pink)}
  .contacts{position:absolute;left:300px;top:52px;list-style:none;color:var(--text-light);font-size:12px;font-weight:300}
  .contacts li{display:flex;align-items:center;gap:8px;height:23px;white-space:nowrap}
  .contacts svg{width:13px;height:13px;flex:none}
  .brand-mark{position:absolute;left:150px;top:178px;font-size:20px;font-weight:300;color:var(--accent-pink);letter-spacing:1px}
  .address{position:absolute;left:30px;right:30px;bottom:28px;color:var(--text-soft);font-size:10.5px;font-weight:300;line-height:1.55;text-align:center}
  .front-brand{position:absolute;left:0;right:0;top:108px;text-align:center;color:var(--white)}
  .front-name{font-size:62px;font-weight:300;letter-spacing:3px}
  .front-tagline{font-size:11px;letter-spacing:4px;margin-top:8px;color:#f3dbec}
</style>
</head>
<body>
  <section class="card card-back">
    <svg class="card-curves" viewBox="0 0 560 320" aria-hidden="true">
      <path d="M-40 300 C120 80 340 20 600 40" fill="none" stroke="#5a5a5e" stroke-width="2"/>
      <path d="M160 -20 C260 120 300 220 280 340" fill="none" stroke="#525256" stroke-width="2"/>
      <path d="M330 -20 C400 140 520 200 600 220 L600 -20 Z" fill="#505054" opacity=".6"/>
    </svg>
    <div class="holder">
      <div class="holder-name">Nim Tressoli</div>
      <div class="holder-title">Creative Director</div>
      <div class="holder-company">Lorantte Co., LTD</div>
    </div>
    <div class="divider"></div>
    <ul class="contacts">
      <li><svg viewBox="0 0 13 13"><rect x="1" y="3" width="11" height="7" fill="none" stroke="#e9e9ea"/><path d="M1 3 L6.5 7 L12 3" fill="none" stroke="#e9e9ea"/></svg>nim.tressoli@lorantte-example.com</li>
      <li><svg viewBox="0 0 13 13"><rect x="3.5" y="1" width="6" height="11" rx="1" fill="none" stroke="#e9e9ea"/></svg>Mobile: 081 536 2947</li>
      <li><svg viewBox="0 0 13 13"><rect x="1.5" y="1.5" width="10" height="10" fill="#c0508f"/></svg>Instragram: lorantte_label</li>
      <li><svg viewBox="0 0 13 13"><rect x="1.5" y="1.5" width="10" height="10" fill="none" stroke="#e9e9ea"/></svg>Facebook: lorantte</li>
      <li><svg viewBox="0 0 13 13"><path d="M3 1.5 L5 4 L4 5.5 C5 7.5 6 8.5 7.5 9 L9 8 L11.5 10 L10 12 C5.5 11 2 7.5 1 3 Z" fill="#e9e9ea"/></svg>TEL: 02 417 39 86</li>
      <li><svg viewBox="0 0 13 13"><circle cx="6.5" cy="6.5" r="5" fill="none" stroke="#e9e9ea"/><path d="M1.5 6.5 H11.5 M6.5 1.5 C4 4 4 9 6.5 11.5 C9 9 9 4 6.5 1.5" fill="none" stroke="#e9e9ea"/></svg>www.lorantte-example.com</li>
    </ul>
    <div class="brand-mark">Lorantte</div>
    <p class="address">47 Mango Row, 2nd Floor , D Building , Thonburi Court , Soi Ratchada 29.<br>Upper Bangrak , Sathorn , Bangkok 10500 Thailand</p>
  </section>

  <section class="card card-front">
    <svg class="card-curves" viewBox="0 0 560 320" aria-hidden="true">
      <path d="M-40 260 C140 40 360 0 600 30" fill="none" stroke="#c46fae" stroke-width="2" opacity=".6"/>
      <path d="M220 -20 C320 120 360 230 330 340" fill="none" stroke="#b85ba0" stroke-width="2" opacity=".6"/>
      <path d="M380 -20 C440 140 520 190 600 200 L600 -20 Z" fill="#b55a9e" opacity=".5"/>
    </svg>
    <div class="front-brand">
      <div class="front-name">Lorantte</div>
      <div class="front-tagline">A WOMEN FASHION HOUSE</div>
    </div>
  </section>
</body>
</html>
```